Advertisements for dental office (3"x3.75" and 3"x2")
People of all ages looking for a family dentist.
I am looking for advertisements that are clean and sophisticated. Most dental ads are cluttered looking and list all the procedures that a dentist will perform. I do not want clutter. I want an ad that speaks for itself and has a lot of emotional appeal. The ads should be simple but still catch your eye.

```html
<!DOCTYPE html>
<html lang="en">
<head>
<meta charset="utf-8">
<title>Martin T. Revin, DDS – Advertisements</title>
<link rel="stylesheet" href="https://fonts.googleapis.com/css2?family=Cinzel:wght@400;700&family=Cormorant+Garamond:ital,wght@0,500;0,600;1,500;1,600&display=swap">
<style>
  :root {
    --backdrop: #3a1f14;
    --paper: #ffffff;
    --magenta: #a3195b;
    --magenta-deep: #7d0f45;
    --maroon: #7a1e3c;
    --ink: #4a4a4a;
    --gold: #e3c04a;
    --skin: #e2b79c;
    --hair: #3d2419;
  }
  * { margin: 0; padding: 0; box-sizing: border-box; }
  html, body { width: 1200px; height: 643px; overflow: hidden; background: var(--backdrop); }
  .stage { position: relative; width: 1200px; height: 643px; }

  .ad { position: absolute; background: var(--paper); overflow: hidden; box-shadow: 0 4px 14px rgba(0,0,0,.45); }

  /* Square ad */
  .ad--square { left: 34px; top: 38px; width: 698px; height: 570px; }
  .ad--square .photo {
    position: absolute; left: 0; top: 0; width: 520px; height: 570px;
    background:
      linear-gradient(90deg, rgba(255,255,255,0) 55%, #fff 100%),
      radial-gradient(ellipse 38% 42% at 42% 48%, var(--skin) 0 60%, transparent 62%),
      linear-gradient(160deg, var(--hair) 0%, #6b4533 45%, #c9b3a6 80%, #f2ebe6 100%);
  }
  .ad--square .copy {
    position: absolute; left: 420px; width: 290px; top: 44px;
    text-align: center; font-family: "Cinzel", serif; color: var(--ink);
  }
  .headline-lead { font-size: 29px; letter-spacing: 1px; line-height: 1; }
  .headline-key { font-size: 60px; font-weight: 700; color: var(--magenta); line-height: 1.05; margin-top: 6px; }
  .headline-tail { font-size: 29px; line-height: 1.35; margin-top: 10px; }

  .signature { position: absolute; left: 420px; width: 290px; top: 355px; text-align: center; font-family: "Cormorant Garamond", serif; color: var(--maroon); }
  .signature .mark { display: block; width: 44px; height: 44px; margin: 0 auto 8px; border-radius: 50%; background: var(--maroon); }
  .practice-name { font-family: "Cinzel", serif; font-size: 19px; }
  .practice-tagline { font-family: "Cinzel", serif; font-size: 18px; line-height: 1.3; margin-top: 8px; color: var(--ink); }
  .practice-address { font-size: 17px; color: var(--ink); margin-top: 18px; }
  .practice-phone { font-family: "Cinzel", serif; font-size: 21px; color: var(--magenta); margin-top: 4px; }

  /* Tall ad */
  .ad--tall { left: 768px; top: 38px; width: 402px; height: 570px; }
  .ad--tall .photo {
    position: absolute; left: 0; top: 70px; width: 402px; height: 402px;
    background:
      linear-gradient(180deg, #fff 0%, rgba(255,255,255,0) 18%),
      radial-gradient(ellipse 30% 40% at 45% 52%, var(--skin) 0 60%, transparent 62%),
      linear-gradient(160deg, var(--hair) 0%, #6b4533 50%, #d8cac1 100%);
  }
  .ad--tall .copy { position: absolute; top: 12px; left: 0; width: 100%; text-align: center; font-family: "Cormorant Garamond", serif; font-style: italic; font-weight: 600; color: var(--ink); }
  .tall-lead { font-size: 26px; }
  .tall-key { font-size: 44px; color: var(--magenta); }
  .tall-tail { font-size: 27px; line-height: 1; }

  .ad--tall .band {
    position: absolute; left: 0; bottom: 0; width: 100%; height: 98px;
    background: linear-gradient(90deg, var(--magenta-deep), var(--magenta) 45%, #c53d7d);
    color: #fff; font-family: "Cinzel", serif;
  }
  .band-tagline { position: absolute; left: 0; width: 100%; top: -22px; text-align: center; font-size: 15px; font-weight: 700; color: var(--gold); }
  .band .mark { position: absolute; left: 22px; top: 26px; width: 46px; height: 46px; border-radius: 50%; background: #fff; }
  .band-info { position: absolute; left: 90px; right: 12px; top: 14px; text-align: center; }
  .band-info .practice-name { font-size: 17px; }
  .band-info .practice-address { font-family: "Cormorant Garamond", serif; font-size: 15px; color: #fff; margin-top: 6px; }
  .band-info .practice-phone { font-size: 17px; color: #fff; margin-top: 2px; }
</style>
</head>
<body>
<main class="stage">
  <section class="ad ad--square">
    <div class="photo" role="img" aria-label="Portrait photo of a smiling young woman with long brown hair"></div>
    <div class="copy">
      <p class="headline-lead">A Beautiful</p>
      <p class="headline-key">SMILE</p>
      <p class="headline-tail">Today, It's Easier<br>Than Ever</p>
    </div>
    <div class="signature">
      <span class="mark"></span>
      <p class="practice-name">Martin T. Revin, DDS, PLLC</p>
      <p class="practice-tagline">Comprehensive Dentistry<br>For All Ages</p>
      <p class="practice-address">212 West Alder Street, Brookhaven</p>
      <p class="practice-phone">555-014-2286</p>
    </div>
  </section>

  <section class="ad ad--tall">
    <div class="photo" role="img" aria-label="Portrait photo of a smiling young woman with long brown hair"></div>
    <div class="copy">
      <p><span class="tall-lead">A Beautiful </span><span class="tall-key">Smile</span></p>
      <p class="tall-tail">Today, It's Easier Than Ever</p>
    </div>
    <div class="band">
      <p class="band-tagline">Comprehensive Dentistry for ALL AGES</p>
      <span class="mark"></span>
      <div class="band-info">
        <p class="practice-name">Martin T. Revin, DDS, PLLC</p>
        <p class="practice-address">212 West Alder Street, Brookhaven</p>
        <p class="practice-phone">555-014-2286</p>
      </div>
    </div>
  </section>
</main>
</body>
</html>
```